fernvale junk clearing

A 6 flyer design.......
I have up loaded our company logo ....must use
A location map...........must use
and our business card with our contact information......please add all contact info
our ph. number must bold and prominent feature.....use use

A reliable Asbestos Removal & Demolition service that you can trust. All our services are offered at realistic prices and delivered on time. We operate 24 / 7 and provide free no-obligation quotes with good old fashion service.

We service the following towns and surrounding areas 7
days a week & 24 hours
Kempsey
Taree
South West Rocks
foster / Tuncurry
Coffs harbour
Nambucca Heads
Newcastle
Maitland
Singleton
Muswellbrook
Upper Hunter Valley
Central Coast
Tamworth
Armidale
this is an easy design as I have most of the theme and colours

```html
<!DOCTYPE html>
<html lang="en">
<head>
<meta charset="utf-8">
<title>Fernvale Junk Clearing – A6 Flyer</title>
<link rel="stylesheet" href="https://fonts.googleapis.com/css2?family=Roboto:wght@300;400;500;700;900&display=swap">
<style>
  :root {
    --green: #17904a;
    --yellow: #f6d70c;
    --ink: #222222;
    --body-ink: #4a4a4a;
    --paper-light: #fbfbfb;
    --paper-dark: #d9d9d9;
    --page: #ffffff;
  }
  * { box-sizing: border-box; margin: 0; padding: 0; }
  html, body {
    width: 1200px; height: 1000px; overflow: hidden;
    background: var(--page);
    font-family: "Roboto", Arial, sans-serif;
  }
  .flyer {
    position: absolute;
    width: 690px; height: 480px;
    background: radial-gradient(ellipse at 50% 45%, var(--paper-light) 0%, #ececec 60%, var(--paper-dark) 100%);
    border: 1px solid #d0d0d0;
  }
  .flyer--front { left: 30px; top: 20px; }
  .flyer--back { left: 480px; top: 510px; }
  .frame-green {
    position: absolute; inset: 14px;
    border: 6px solid var(--green);
  }
  .frame-yellow {
    position: absolute; inset: 26px;
    border: 5px solid var(--yellow);
  }
  .front-content {
    position: absolute; inset: 40px 40px 30px;
    text-align: center;
  }
  .brand-name {
    color: var(--green);
    font-weight: 900;
    text-transform: uppercase;
    line-height: 1;
  }
  .brand-name__top { display: block; font-size: 64px; letter-spacing: 1px; margin-top: 6px; }
  .brand-name__bottom { display: block; font-size: 46px; letter-spacing: 4px; margin-top: 6px; }
  .tagline {
    margin-top: 28px;
    font-size: 24px; font-weight: 700; color: var(--ink);
    line-height: 1.38; letter-spacing: 0.5px; text-transform: uppercase;
  }
  .phone {
    color: var(--green); font-weight: 700; letter-spacing: 2px;
  }
  .front-content .phone { margin-top: 24px; font-size: 40px; line-height: 1; }
  .website {
    margin-top: 10px; font-size: 20px; font-weight: 500; color: var(--ink); letter-spacing: 0.5px;
  }
  .credentials {
    margin-top: 24px; font-size: 14px; color: var(--ink); line-height: 1.6;
    letter-spacing: 0.4px; text-transform: uppercase;
  }
  .back-content {
    position: absolute; inset: 46px 44px 36px;
  }
  .intro {
    font-size: 19px; font-weight: 300; color: var(--body-ink); line-height: 1.45;
  }
  .intro strong { font-weight: 700; color: var(--ink); }
  .service-heading {
    margin-top: 16px; font-size: 14px; font-weight: 700; color: var(--green);
  }
  .service-area {
    display: flex; margin-top: 12px; gap: 20px;
  }
  .service-map {
    width: 210px; height: 215px; flex: none;
    background: linear-gradient(90deg, #dfe8c9 0%, #c9dca5 55%, #a9cff0 80%, #a9cff0 100%);
  }
  .town-list {
    list-style: none; font-size: 15px; font-weight: 500; color: var(--ink); line-height: 1.6;
  }
  .towns { display: flex; gap: 44px; }
  .flyer--back .phone {
    position: absolute; right: 0; bottom: 0; font-size: 38px;
  }
</style>
</head>
<body>

<section class="flyer flyer--front">
  <div class="frame-green"></div>
  <div class="frame-yellow"></div>
  <div class="front-content">
    <h1 class="brand-name">
      <span class="brand-name__top">Fernvale Junk</span>
      <span class="brand-name__bottom">Clearing</span>
    </h1>
    <p class="tagline">A reliable asbestos removal &amp;<br>demolition service that you can trust!</p>
    <p class="phone">TEL: 0412555019</p>
    <p class="website">www.fernvalejunkclearing.com</p>
    <p class="credentials">Aust owned and operated. Fully licenced and insured.<br>A trusted local name servicing the Mid North Coast and beyond...</p>
  </div>
</section>

<section class="flyer flyer--back">
  <div class="frame-green"></div>
  <div class="frame-yellow"></div>
  <div class="back-content">
    <p class="intro">We are a reliable Asbestos Removal &amp; Demolition service that you can trust. All our services are offered at realistic prices and delivered on time. We operate 24/7 and provide <strong>FREE</strong> no-obligation quotes with good old fashion service.</p>
    <p class="service-heading">We service the following towns and surrounding areas 7 days a week and 24 hours:</p>
    <div class="service-area">
      <div class="service-map" role="img" aria-label="Map of the New South Wales coast showing the service area circle"></div>
      <div class="towns">
        <ul class="town-list">
          <li>Kempsey</li>
          <li>Taree</li>
          <li>South West Rocks</li>
          <li>Foster / Tuncurry</li>
          <li>Coffs Harbour</li>
          <li>Nambucca Heads</li>
          <li>Newcastle</li>
        </ul>
        <ul class="town-list">
          <li>Maitland</li>
          <li>Singleton</li>
          <li>Muswellbrook</li>
          <li>Upper Hunter Valley</li>
          <li>Central Coast</li>
          <li>Tamworth</li>
          <li>Armidale</li>
        </ul>
      </div>
    </div>
    <p class="phone">TEL: 0412555019</p>
  </div>
</section>

</body>
</html>
```